Fundraising Event Logistics and Strategy

We need a web design for our non-profit fundraising event strategy business. We help non-profits streamline gala and 'pre registered' event operations to maximize their funds raised. We would like a simple design, our company colors are dark blue and silver. The design should be clean and also allow for some partner logos. I have attached some current logo collateral. Company is Dana Whitcombe & Co dba GalaPivotry, but neither logo has to be used.
Target Market(s)
Non Profit Organizations
Industry/Entity Type
Business
Number of Pages Required
3 page
Requirements
Must have
- Contact Us Form
- Partner Logos with Links

```html
<!DOCTYPE html>
<html lang="en">
<head>
<meta charset="utf-8">
<title>GalaPivotry — Fundraising Event Logistics and Strategy</title>
<link href="https://fonts.googleapis.com/css2?family=Open+Sans:wght@400;600;700&family=Marcellus&display=swap" rel="stylesheet">
<style>
:root{
  --blue:#0b55a8;
  --blue-dark:#084585;
  --silver:#c9ccd1;
  --ink:#333a44;
  --muted:#7b818a;
  --bg:#ffffff;
  --footer:#2b2d31;
  --footer-line:#3d4046;
}
*{margin:0;padding:0;box-sizing:border-box}
html,body{width:1200px;height:2228px;overflow:hidden;background:var(--bg)}
body{font-family:"Open Sans",Arial,sans-serif;color:var(--ink);position:relative}
.topbar{height:32px;background:var(--blue);color:#fff;font-size:12px;display:flex;justify-content:space-between;align-items:center;padding:0 240px}
.topbar span{display:flex;align-items:center;gap:8px}
.dot{width:14px;height:14px;border-radius:50%;background:#fff;display:inline-block}
.header{height:88px;display:flex;align-items:center;justify-content:space-between;padding:0 240px;border-bottom:1px solid #e4e6ea}
.brand{font-family:"Open Sans",sans-serif;font-weight:600;font-size:20px;color:var(--ink);display:flex;align-items:center;gap:10px}
.brand i{width:14px;height:14px;background:var(--blue);display:inline-block}
.nav{display:flex;gap:24px;font-size:15px}
.nav a{color:var(--ink);text-decoration:none}
.nav a.active{color:var(--blue);border-bottom:2px solid var(--blue);padding-bottom:4px}
.hero{height:480px;position:relative;background:radial-gradient(ellipse at 50% 55%,#f6e2cf 0%,#f3d8bf 35%,#fbf1e7 70%,#fff 100%)}
.hero h1{position:absolute;top:246px;width:100%;text-align:center;font-family:"Marcellus",serif;font-weight:400;font-size:84px;color:#2c3039;letter-spacing:2px}
.who{height:240px;text-align:center;padding-top:28px}
.section-title{font-size:36px;font-weight:400;color:var(--ink)}
.who .rule{width:90px;height:2px;background:var(--blue);margin:10px auto 14px}
.who p{width:760px;margin:0 auto;font-size:13px;line-height:19px;color:var(--muted)}
.btn{display:inline-block;background:var(--blue);color:#fff;font-size:13px;padding:7px 26px;border-radius:2px;margin-top:22px;text-decoration:none}
.what{height:440px;background:var(--blue);text-align:center;padding-top:72px}
.what .section-title{color:#fff}
.what .rule{width:480px;height:1px;background:rgba(255,255,255,.6);margin:14px auto 22px}
.cards{display:flex;justify-content:center;gap:28px}
.card{width:214px;background:#fff;padding:8px}
.card .ph{height:148px}
.card p{font-size:12px;line-height:16px;color:var(--muted);padding:16px 10px 12px}
.split{height:292px;display:flex;padding:28px 240px 0;gap:40px}
.partners{flex:1}
.split h2{font-size:22px;font-weight:400;color:var(--ink);padding-bottom:8px;border-bottom:1px solid #d5d8dd}
.logos{display:flex;gap:20px;margin-top:40px}
.logos a{width:148px;height:148px;border:1px solid #d5d8dd;display:flex;align-items:center;justify-content:center}
.logos span{width:90px;height:70px;background:var(--silver);display:block}
.news{width:200px}
.item{display:flex;gap:12px;margin-top:24px}
.thumb{width:40px;height:48px;border:1px solid #d5d8dd;display:flex;align-items:flex-end}
.thumb b{width:100%;height:18px;background:var(--blue);color:#fff;font-size:8px;font-weight:600;text-align:center;line-height:18px}
.item h3{font-size:12px;font-weight:600;color:var(--ink)}
.item p{font-size:11px;line-height:14px;color:var(--muted)}
.contact{height:388px;position:relative;background:linear-gradient(180deg,#2a1e18 0%,#6b4a35 45%,#a9835f 62%,#3a2a21 100%);text-align:center;padding-top:22px;color:#fff}
.contact h2{font-size:24px;font-weight:400}
.contact .lead{font-size:16px;margin-top:6px}
.form{width:688px;margin:18px auto 0;background:#fff;padding:18px 20px 14px;text-align:left;display:grid;grid-template-columns:1fr 1fr;column-gap:36px}
.form label{font-size:11px;color:var(--ink);display:block;margin-bottom:4px}
.form .f{margin-bottom:14px}
.form .line{height:22px;border:1px solid #dde0e4}
.form .full{grid-column:1/3}
.form .full .line{height:44px}
.form .submit{background:var(--blue);color:#fff;font-size:13px;border:0;padding:7px 34px;justify-self:start;border-radius:2px;font-family:inherit}
.footer{height:268px;background:var(--footer);color:#a9adb3;padding:30px 240px 0;position:relative}
.cols{display:flex;gap:30px}
.col h4{color:#fff;font-size:14px;font-weight:400;margin-bottom:12px}
.col ul{list-style:none;font-size:11px;line-height:21px}
.col li::before{content:"•";color:var(--blue);margin-right:8px}
.col.c1{width:150px}.col.c2{width:190px}.col.c3{width:190px}.col.c4{flex:1}
.contact-row{display:flex;gap:8px;font-size:11px;line-height:15px;margin-bottom:10px}
.contact-row i{width:16px;height:16px;border-radius:50%;background:#4a4d53;flex:none}
.qc{height:22px;background:#3a3d43;margin-bottom:8px;font-size:10px;padding:4px 8px;color:#8d9198}
.qc-btn{width:70px;height:22px;background:#55585e}
.bottom{position:absolute;left:240px;right:240px;bottom:0;height:42px;border-top:1px solid var(--footer-line);display:flex;justify-content:space-between;align-items:center;font-size:11px}
.social{display:flex;gap:8px}
.social span{width:20px;height:20px;border-radius:50%;background:#55585e}
</style>
</head>
<body>
<div class="topbar">
  <span><i class="dot"></i>hello@galapivotry.org</span>
  <span><i class="dot"></i>727-555-0142</span>
</div>
<header class="header">
  <div class="brand"><i></i>Dana Whitcombe &amp; Co</div>
  <nav class="nav">
    <a class="active" href="#">Home</a><a href="#">Who We Are</a><a href="#">Why Choose Us</a><a href="#">News</a><a href="#">Contact</a>
  </nav>
</header>
<section class="hero" role="img" aria-label="Photo of cupped hands holding a paper cut-out family on a warm, soft background">
  <h1>We are happy to help</h1>
</section>
<section class="who">
  <h2 class="section-title">Who We Are</h2>
  <div class="rule"></div>
  <p>We help non-profit organizations plan and run galas and pre registered events from start to finish. Our team streamlines guest check-in, bidding, payments and reporting so your staff can focus on donors and your mission, and every event raises more for the cause you serve.</p>
  <a class="btn" href="#">Read More</a>
</section>
<section class="what">
  <h2 class="section-title">What We Do</h2>
  <div class="rule"></div>
  <div class="cards">
    <div class="card"><div class="ph" role="img" aria-label="Photo of two people reviewing notes at a desk" style="background:linear-gradient(135deg,#cfd6dc,#8f9aa5)"></div><p>5 Millennial Donor Engagement Strategies That Work</p></div>
    <div class="card"><div class="ph" role="img" aria-label="Photo of a group of volunteers on a green lawn" style="background:linear-gradient(135deg,#6f9a4e,#3f6b34)"></div><p>5 Millennial Donor Engagement Strategies That Work</p></div>
    <div class="card"><div class="ph" role="img" aria-label="Photo of smiling supporters at an outdoor event" style="background:linear-gradient(135deg,#d9c7b4,#9b8a7a)"></div><p>5 Millennial Donor Engagement Strategies That Work</p></div>
  </div>
</section>
<section class="split">
  <div class="partners">
    <h2>Our Partner</h2>
    <div class="logos">
      <a href="#" aria-label="Partner one"><span></span></a>
      <a href="#" aria-label="Partner two"><span></span></a>
      <a href="#" aria-label="Partner three"><span></span></a>
    </div>
  </div>
  <div class="news">
    <h2>Latest News</h2>
    <div class="item"><div class="thumb"><b>News</b></div><div><h3>News Headlines Here</h3><p>Short news summary text<br>goes in this small space.</p></div></div>
    <div class="item"><div class="thumb"><b>News</b></div><div><h3>News Headlines Here</h3><p>Short news summary text<br>goes in this small space.</p></div></div>
  </div>
</section>
<section class="contact" role="img" aria-label="Photo of a person raising arms against a dusky sunset sky">
  <h2>Contact Us</h2>
  <p class="lead">If you think we can help We'd love to hear from you</p>
  <form class="form">
    <div class="f"><label>Name</label><div class="line"></div></div>
    <div class="f"><label>Email</label><div class="line"></div></div>
    <div class="f"><label>Phone</label><div class="line"></div></div>
    <div class="f"><label>City</label><div class="line"></div></div>
    <div class="f full"><label>Details</label><div class="line"></div></div>
    <button class="submit" type="button">Submit</button>
  </form>
</section>
<footer class="footer">
  <div class="cols">
    <div class="col c1"><h4>Main menu</h4><ul><li>Home</li><li>About Us</li><li>Who We Are</li><li>Why choose us</li><li>News</li></ul></div>
    <div class="col c2"><h4>Information</h4><ul><li>Policies</li><li>Legal Notice</li><li>Terms and conditions</li><li>Benefits of services</li></ul></div>
    <div class="col c3"><h4>Contact us</h4>
      <div class="contact-row"><i></i><span>1450 Harbor Crest Blvd<br>Tampa, FL 33602</span></div>
      <div class="contact-row"><i></i><span>727-555-0142</span></div>
      <div class="contact-row"><i></i><span>hello@galapivotry.org</span></div>
    </div>
    <div class="col c4"><h4>Quick Contact</h4><div class="qc">Your name</div><div class="qc">Your email</div><div class="qc-btn"></div></div>
  </div>
  <div class="bottom">
    <span>© 2024 Dana Whitcombe &amp; Co. All rights reserved.</span>
    <div class="social"><span></span><span></span><span></span><span></span><span></span><span></span></div>
  </div>
</footer>
</body>
</html>
```